Homepage Design for Digital Advertising Company

The website will be very simple, with just one page (the homepage).

We are a new startup company, Brightlane Media, and focus on social media and gaming advertising. We work directly with brands, and with other media agencies. I have attached some details about our company, what we do, and content you can use for the website. I have also attached a screenshot of our logo (high quality files will be provided shortly).

This is an example of a website we really like. They do not do what we do, however their layout is great, and the best part about it is that they really get the message accross of exactly what they do as soon as the page loads. We do not have a product video, so that part does not apply, however i love their basic page layout.
http://www.vorelqin.com/

We can say something like this:
Simple Social Media and Gaming Advertising (BIG TEXT)
WE DELIVER: Plumbook fans and likes, Chirpel followers, Targeted ads and video, and more... (SubText)

On the homepage, we want to have a prominent "Free Consultation" box with a "Submit" button. This box will have input boxes for:
Name
Email
Phone
Or, we can do just a simple email submit as seen here (I like how they did a one long page design BTW)
http://mornivex.com/

Here are some other sites i like:
http://www.tabrolin.com/
http://www.kelvaro.com/
http://graystitch.net/

Not sure what you will get out of this one, but its too unique to not mention:
http://yulomar.com/handset/

COLORS:
We are flexible on color scheme. We can change the color of the logo, so dont let that limit your color concepts.

Content on site:
We can use fly out buttons or "more" links for extra text dropdowns if you only want to include an excerpt from each topic in the attached content sheet. Dont want page to be too busy.

Long One Page:
We are not opposed to something like this, by the way
http://mornivex.com/

Target Market(s)

big brands, advertising agencies

Industry/Entity Type

Digital

Requirements
Must have
• Logo
Sign up form
Nice to have
• all the content from our attachment
Should not have
• busy designs, lack of white space, too much text

```html
<!DOCTYPE html>
<html lang="en">
<head>
<meta charset="utf-8">
<title>Brightlane Media – Simple Social Media &amp; Gaming Advertising</title>
<link href="https://fonts.googleapis.com/css2?family=Audiowide&family=Encode+Sans+Condensed:wght@300;400&family=Open+Sans:wght@400;600&display=swap" rel="stylesheet">
<style>
  :root {
    --green-deep: #7fb000;
    --green-glow: #c6e20a;
    --green-dark: #1d5a12;
    --ribbon-red: #8c2326;
    --ribbon-fold: #5e1416;
    --bar-black: #1a1d1f;
    --blue-deep: #0b4f6e;
    --blue-mid: #0f6682;
    --blue-glow: #22b4d8;
    --white: #ffffff;
    --lime: #b6e43c;
    --logo-ink: #1f2a24;
  }
  * { margin: 0; padding: 0; box-sizing: border-box; }
  html, body { width: 1180px; height: 1200px; overflow: hidden; }
  body { font-family: "Open Sans", Arial, sans-serif; position: relative; background: var(--blue-deep); }

  .hero {
    position: absolute; left: 0; top: 0; width: 1180px; height: 608px;
    background:
      radial-gradient(ellipse 420px 340px at 720px 380px, var(--green-glow) 0%, rgba(198,226,10,0) 100%),
      linear-gradient(180deg, #86b600 0%, var(--green-deep) 100%);
    box-shadow: 0 4px 10px rgba(0,0,0,0.25);
  }
  .brand {
    position: absolute; left: 111px; top: 54px;
    font-family: "Open Sans", Arial, sans-serif; font-weight: 400;
    font-size: 38px; color: var(--logo-ink); letter-spacing: -0.5px;
  }
  .nav-ribbon { position: absolute; left: 64px; top: 80px; }
  .nav {
    position: absolute; left: 81px; top: 115px; width: 991px; height: 37px;
    display: flex; align-items: center; list-style: none;
  }
  .nav li {
    position: absolute; transform: translateX(-50%);
    color: var(--white); font-size: 17px; white-space: nowrap; letter-spacing: 0.2px;
  }
  .headline {
    position: absolute; left: 81px; top: 196px;
    font-family: "Audiowide", sans-serif; font-weight: 400;
    font-size: 80px; line-height: 72px; text-transform: uppercase;
    color: var(--white); letter-spacing: 1px;
    text-shadow: 2px 3px 4px rgba(40,70,0,0.45);
  }
  .headline .amp { color: var(--green-dark); }
  .deliver { position: absolute; left: 714px; top: 202px; width: 380px; }
  .deliver-title {
    font-family: "Audiowide", sans-serif; font-size: 32px; line-height: 34px;
    color: var(--green-dark); text-transform: uppercase; letter-spacing: 1px;
  }
  .deliver-text {
    margin-top: 6px; font-size: 18px; line-height: 19px; color: var(--white);
  }

  .about {
    position: absolute; left: 0; top: 608px; width: 1180px; height: 592px;
    background:
      radial-gradient(ellipse 360px 300px at 612px 560px, var(--blue-glow) 0%, rgba(34,180,216,0) 100%),
      linear-gradient(180deg, var(--blue-mid) 0%, var(--blue-deep) 100%);
  }
  .about-title {
    position: absolute; left: 81px; top: 70px;
    font-family: "Audiowide", sans-serif; font-size: 64px; line-height: 64px;
    color: transparent; -webkit-text-stroke: 1.5px var(--white);
    text-transform: uppercase; letter-spacing: 1px;
  }
  .about-copy {
    position: absolute; left: 81px; top: 156px; width: 1000px;
    font-family: "Encode Sans Condensed", sans-serif; font-weight: 300;
    font-size: 23px; line-height: 28px; color: var(--white);
  }
  .about-copy p + p { margin-top: 44px; }
  .about-copy .highlight { color: var(--lime); font-size: 36px; line-height: 44px; }
</style>
</head>
<body>
  <header class="hero">
    <div class="brand">Brightlane Media</div>

    <svg class="nav-ribbon" width="1052" height="100" viewBox="0 0 1052 100" aria-hidden="true">
      <polygon points="0,2 24,2 24,40 17,34 0,34" fill="var(--ribbon-red)"/>
      <polygon points="0,34 17,34 24,40 17,40" fill="var(--ribbon-fold)"/>
      <polygon points="1052,2 1028,2 1028,40 1035,34 1052,34" fill="var(--ribbon-red)"/>
      <polygon points="1052,34 1035,34 1028,40 1035,40" fill="var(--ribbon-fold)"/>
      <rect x="26" y="72" width="973" height="16" fill="var(--bar-black)"/>
      <polygon points="92,88 130,88 111,98" fill="var(--bar-black)"/>
      <rect x="17" y="35" width="991" height="37" fill="var(--ribbon-red)"/>
    </svg>

    <ul class="nav">
      <li style="left:96px">HOME</li>
      <li style="left:239px">ABOUT US</li>
      <li style="left:456px">HOW WE CAN HELP YOU</li>
      <li style="left:690px">HOW IT WORKS</li>
      <li style="left:869px">CONTACT</li>
    </ul>

    <h1 class="headline">Simple<br>Social<br>Media <span class="amp">&amp;</span><br>Gaming<br>Advertising</h1>

    <div class="deliver">
      <h2 class="deliver-title">We Deliver</h2>
      <p class="deliver-text">Plumbook fans and likes, Chirpel followers,<br>Targeted ads and video, and more...</p>
    </div>
  </header>

  <section class="about">
    <h2 class="about-title">About Us</h2>
    <div class="about-copy">
      <p>As a media buyer, it is extremely important to attract the most targeted audience possible while maximizing your return on investment.&nbsp; We accomplish this by getting your brand in front of your most profitable customers where they spend most of their leisure time, playing games.&nbsp; There are over 100 million people who play games on Plumbook everyday for 30 minutes on average.&nbsp; That does not include the casual gamer who plays less often, or gamers on other sites and networks we work with.</p>
      <p>We are able to effectively target any demographic through social gaming from tweens to seniors while they are most focused and engaged.&nbsp; Our platform is capable of attracting your audience using <span class="highlight">interactive video, display ads, Plumbook likes, chirpel follows, and in game sponsorships.</span></p>
    </div>
  </section>
</body>
</html>
```